依頼概要
■依頼の目的/概要
小学生バレーボールのスポーツ少年団でメンバーを募集するためのポスターの作成をお願いします。

■依頼詳細
ポスターは男子チーム、女子チーム兼用となります。主に教室での直接配布、校内の掲示板や近隣の施設(コンビニや公民館等)での掲示を目的としたものになります。

必要に応じて写真の背景等を加工いただいても構いません。

楽しそうなイメージだけでなく、スポーツに関心のある子どもたちがバレーボールを“かっこいい”と感じてくれるような躍動感の伝わるものを希望しています。

■重視する点
・明るくインパクトのあるデザイン
・できるだけ躍動感の伝わるもの
・読みやすい文字であること

■サイズ
A4サイズでお願いします。
メインはA4ですが、B4(A4の122%)にも対応する画素数でお願いいたします

■その他
・レイアウトイメージ、素材は添付ファイルにてご確認ください
・写真やイラストの素材は当方で用意していますが、用意したもの以外の素材を使っていただいても構いません。
・レイアウトのイメージやキャッチコピー、掲載する文言等は添付の「レイアウトイメージ.pdf」「レイアウト説明.txt」を参照ください。レイアウトは当方のイメージと異なるものになっても構いません。

何かご不明な点がございましたら、お気軽にご質問下さい。
どうぞよろしくお願いいたします。
納品いただくデータですが、納品後に当方で編集することがあるため、フォトショップまたはイラストレーターで編集できるかたちで納品いただけますと幸いです。よろしくお願いします。

```html
<!DOCTYPE html>
<html lang="ja">
<head>
<meta charset="UTF-8">
<title>若葉バレースポーツ少年団 新メンバー募集</title>
<link rel="stylesheet" href="https://fonts.googleapis.com/css2?family=Dela+Gothic+One&family=Noto+Sans+JP:wght@500;700;900&display=swap">
<style>
:root{
  --red:#e0172b;
  --red-deep:#b5101f;
  --navy:#141a3c;
  --yellow:#ffe100;
  --white:#ffffff;
  --ink:#111111;
  --photo-a:#8a5a4a;
  --photo-b:#3b3f66;
  --illus-skin:#f3c9a8;
}
*{margin:0;padding:0;box-sizing:border-box}
html,body{width:849px;height:1200px;overflow:hidden;background:var(--white)}
body{font-family:"Noto Sans JP",sans-serif;color:var(--ink)}
.poster{position:relative;width:849px;height:1200px;overflow:hidden;background:var(--white)}
.bg{position:absolute;inset:0}
.emblem{position:absolute;left:18px;top:12px;width:34px;height:34px;border-radius:50%;background:var(--white);border:3px solid var(--red)}
.headline{position:absolute;left:70px;top:20px;font-family:"Dela Gothic One",sans-serif;transform:skewX(-8deg);line-height:1.02;letter-spacing:2px;z-index:2}
.headline span{display:block;white-space:nowrap}
.headline .l1{font-size:68px;color:var(--ink)}
.headline .l2{font-size:84px;color:var(--red);-webkit-text-stroke:2px var(--white);margin-left:-20px}
.headline .l3{font-size:68px;color:var(--ink);margin-left:270px;-webkit-text-stroke:2px var(--white)}
.illus{position:absolute}
.ball-top{left:606px;top:14px;width:92px;height:92px;border-radius:50%;background:radial-gradient(circle at 35% 35%,#ffe56a,#f2b600 60%,#1d4fa5 100%)}
.player-top{left:610px;top:90px;width:160px;height:170px;border-radius:40% 50% 30% 40%;background:linear-gradient(160deg,var(--illus-skin),#c8344a 70%)}
.photo{position:absolute;background:linear-gradient(160deg,var(--photo-a),var(--photo-b));border:3px solid var(--white)}
.p1{left:24px;top:250px;width:190px;height:170px}
.p2{left:60px;top:300px;width:200px;height:260px;border:none;background:linear-gradient(170deg,#c8344a,#2b2d55)}
.p3{left:245px;top:280px;width:145px;height:180px;background:linear-gradient(170deg,#d23b3b,#3a2f4f)}
.p4{left:440px;top:265px;width:185px;height:230px;background:linear-gradient(160deg,#6b6f8f,#2d2540)}
.p5{left:630px;top:300px;width:190px;height:180px;background:linear-gradient(160deg,#9c6b55,#3c3455)}
.p6{left:20px;top:480px;width:210px;height:120px;background:linear-gradient(160deg,#4a4e73,#b3283a)}
.p7{left:500px;top:500px;width:325px;height:125px;background:linear-gradient(160deg,#5d5f80,#b02a3d)}
.callout{position:absolute;font-weight:900;color:var(--white);text-shadow:0 0 3px var(--navy),0 0 6px var(--navy);white-space:nowrap;z-index:3}
.c1{left:20px;top:300px;font-size:16px;transform:rotate(-14deg);line-height:1.3}
.c2{left:310px;top:250px;font-size:26px;color:var(--yellow);transform:rotate(-14deg);line-height:1.2}
.c3{left:782px;top:100px;font-size:14px;writing-mode:vertical-rl;color:var(--ink);text-shadow:0 0 3px var(--white),0 0 5px var(--white);line-height:1.3}
.c3 .tcy{text-combine-upright:all}
.c4{left:640px;top:632px;font-size:12px}
.recruit{position:absolute;left:0;top:670px;width:849px;text-align:center}
.team{font-size:27px;font-weight:900;color:var(--white);letter-spacing:1px;margin-left:-120px}
.headcopy{font-family:"Dela Gothic One",sans-serif;font-size:50px;color:var(--yellow);letter-spacing:1px;margin-left:-120px;-webkit-text-stroke:1px var(--navy);margin-top:-4px}
.visit{position:absolute;left:700px;top:662px;width:118px;height:118px;border-radius:50%;background:var(--yellow);display:flex;align-items:center;justify-content:center;text-align:center;font-weight:900;font-size:16px;line-height:1.25;color:var(--ink)}
.schedule{position:absolute;left:218px;top:800px;width:600px;background:var(--white);border-collapse:collapse}
.schedule td{font-weight:700;font-size:14px;padding:9px 8px;border-bottom:2px solid var(--navy);line-height:1.3}
.schedule .day{width:100px;text-align:center;white-space:nowrap}
.schedule .day span{display:inline-block;background:var(--red);color:var(--white);padding:1px 8px;border-radius:3px;font-size:13px}
.schedule .item span{background:var(--navy)}
.schedule .time{font-size:18px;font-weight:900;width:110px}
.label{position:absolute;left:116px;top:806px;width:90px;height:90px;background:var(--white);display:flex;flex-direction:column;align-items:center;justify-content:center;font-weight:900;font-size:20px;line-height:1.2}
.label small{font-size:16px}
.player-bottom{left:20px;top:990px;width:190px;height:140px;border-radius:50% 40% 40% 50%;background:linear-gradient(200deg,var(--illus-skin),#c8344a 75%)}
.ball-bottom{left:110px;top:968px;width:56px;height:56px;border-radius:50%;background:radial-gradient(circle at 35% 35%,#ffe56a,#f2b600 60%,#1d4fa5 100%)}
.message{position:absolute;left:240px;top:1000px;width:340px;font-size:11.5px;font-weight:500;line-height:1.7}
.group{position:absolute;left:590px;top:995px;width:245px;height:130px;background:linear-gradient(180deg,#c9d8ea,#4a4e73 60%,#2d2540)}
.contact{position:absolute;left:0;top:1134px;width:600px;height:66px;background:var(--red);color:var(--white);display:flex;align-items:center}
.contact .tag{writing-mode:vertical-rl;font-size:13px;font-weight:900;padding:0 6px 0 10px;letter-spacing:2px}
.contact .team-name{font-size:17px;font-weight:900}
.contact .tel{font-size:26px;font-weight:900;display:flex;align-items:center;gap:4px;line-height:1.1}
.contact-body{padding-left:8px}
.chair{position:absolute;left:488px;top:1141px;width:92px;height:52px;background:var(--white);color:var(--ink);text-align:center;font-size:10px;font-weight:700;line-height:1.25;padding-top:3px}
.chair b{display:block;font-size:16px;font-weight:900;line-height:1.2}
</style>
</head>
<body>
<main class="poster">
  <svg class="bg" width="849" height="1200" viewBox="0 0 849 1200" aria-hidden="true">
    <polygon points="600,0 849,0 849,70" fill="var(--red)"/>
    <polygon points="0,200 849,150 849,965 0,965" fill="var(--navy)"/>
    <polygon points="0,215 849,165 849,230 0,300" fill="var(--red)"/>
    <polygon points="0,600 849,560 849,640 0,690" fill="var(--red-deep)"/>
    <polygon points="0,965 849,965 849,975 0,990" fill="var(--red)"/>
  </svg>

  <div class="emblem" aria-hidden="true"></div>

  <h1 class="headline">
    <span class="l1">そうだ、</span>
    <span class="l2">バレーボール、</span>
    <span class="l3">しよう。</span>
  </h1>

  <div class="illus ball-top" role="img" aria-label="バレーボールのイラスト"></div>
  <div class="illus player-top" role="img" aria-label="スパイクを打つ女子選手のイラスト"></div>

  <div class="photo p1" role="img" aria-label="試合中の女子選手の写真"></div>
  <div class="photo p2" role="img" aria-label="笑顔でポーズする男子選手たちの写真"></div>
  <div class="photo p3" role="img" aria-label="レシーブ練習の写真"></div>
  <div class="photo p4" role="img" aria-label="体育館でスパイクを打つ選手の写真"></div>
  <div class="photo p5" role="img" aria-label="体育館での練習風景の写真"></div>
  <div class="photo p6" role="img" aria-label="整列するチームの写真"></div>
  <div class="photo p7" role="img" aria-label="ユニフォーム姿のチーム集合写真"></div>

  <p class="callout c1">チョウのようにまい！<br>ハチのようにさそう！</p>
  <p class="callout c2">レシーブ！　スパイク！<br>キマると気もちいい！</p>
  <p class="callout c3">屋内だから<br>夏場や雨の日も安心<span class="tcy">!!</span></p>
  <p class="callout c4">感染症対策もしています。</p>

  <section class="recruit">
    <p class="team">若葉バレースポーツ少年団</p>
    <h2 class="headcopy">男女新メンバー募集!!</h2>
  </section>
  <div class="visit">見学・体験<br>いつでも<br>受付中！</div>

  <div class="label">練習日<small>(毎週)</small></div>
  <table class="schedule">
    <tr><td class="day"><span>土・日曜日</span></td><td>若葉小学校体育館・<br>若葉西小学校体育館</td><td class="time">9:00〜</td></tr>
    <tr><td class="day"><span>水曜日</span></td><td>若葉小学校体育館</td><td class="time">17:30〜</td></tr>
    <tr><td class="day item"><span>持ち物</span></td><td colspan="2">上ぐつ、水とう、動きやすい服そう</td></tr>
  </table>

  <div class="illus player-bottom" role="img" aria-label="レシーブする選手のイラスト"></div>
  <div class="illus ball-bottom" role="img" aria-label="バレーボールのイラスト"></div>

  <p class="message">みんなが元気な笑顔でいられるよう、<br>若葉バレーは仲よく楽しく練習しています。<br>はじめての子もていねいに教えるので、<br>経験がなくても大丈夫です。<br>友だちもさそって気軽に来てね！</p>

  <div class="group" role="img" aria-label="屋外でのチーム集合写真"></div>

  <footer class="contact">
    <span class="tag">連絡先</span>
    <div class="contact-body">
      <p class="team-name">若葉バレースポーツ少年団</p>
      <p class="tel">
        <svg width="22" height="22" viewBox="0 0 24 24" aria-hidden="true"><path fill="var(--white)" d="M6.6 10.8a15.1 15.1 0 0 0 6.6 6.6l2.2-2.2c.3-.3.7-.4 1-.2 1.1.4 2.3.6 3.6.6.6 0 1 .4 1 1V20c0 .6-.4 1-1 1A17 17 0 0 1 3 4c0-.6.4-1 1-1h3.5c.6 0 1 .4 1 1 0 1.3.2 2.5.6 3.6.1.3 0 .7-.2 1z"/></svg>
        090-1234-5678
      </p>
    </div>
  </footer>
  <div class="chair">育成会会長<b>森田</b>まで</div>
</main>
</body>
</html>
```